Modified Business card

We have developed a new logo for the business, and want thou to tray and incorporate it into the business card design that you have done for us.

I am going to upload the logo files. We like the simple clean look that you have on the card, so if you can keep the look incorporating the logo.

Industry/Entity Type

Business

```html
<!DOCTYPE html>
<html lang="en">
<head>
<meta charset="utf-8">
<title>Kestrel Engineering – Business Card</title>
<link rel="stylesheet" href="https://fonts.googleapis.com/css2?family=Source+Sans+3:wght@400;600;700&display=swap">
<style>
  :root {
    --brand-red: #d02027;
    --ink-grey: #58595b;
    --card-edge: #2b2b2b;
    --paper: #ffffff;
  }
  * { margin: 0; padding: 0; box-sizing: border-box; }
  html, body {
    width: 1200px; height: 1000px; overflow: hidden;
    background: var(--paper);
    font-family: "Source Sans 3", sans-serif;
  }
  .canvas { position: relative; width: 1200px; height: 1000px; }

  .card-front {
    position: absolute; left: 214px; top: 46px; width: 773px; height: 441px;
    background: var(--brand-red);
    border-radius: 0 42px 0 42px;
    display: flex; align-items: center; justify-content: center;
  }
  .front-name {
    color: var(--paper); font-weight: 700; font-size: 72px; letter-spacing: 1px;
  }

  .card-back {
    position: absolute; left: 214px; top: 511px; width: 773px; height: 441px;
    background: var(--paper);
    border: 2px solid var(--card-edge);
    border-radius: 0 40px 0 40px;
  }
  .brand {
    position: absolute; left: 31px; top: 35px;
    display: flex; align-items: center; gap: 16px;
  }
  .brand-square {
    width: 98px; height: 97px; background: var(--brand-red); border-radius: 6px;
  }
  .brand-name {
    color: var(--ink-grey); font-weight: 700; font-size: 42px; line-height: 1;
  }

  .person {
    position: absolute; right: 31px; top: 162px; text-align: right; color: var(--ink-grey);
  }
  .person-name { font-weight: 700; font-size: 33px; line-height: 40px; }
  .person-title { font-weight: 400; font-size: 28px; line-height: 38px; }

  .contact {
    position: absolute; right: 31px; top: 274px; text-align: right;
    color: var(--ink-grey); font-weight: 600; font-size: 25px; line-height: 35px;
  }
  .contact .label { margin-right: 10px; }

  .address {
    position: absolute; left: 31px; top: 285px;
    color: var(--brand-red); font-weight: 700; font-size: 24px; line-height: 32px;
  }
</style>
</head>
<body>
<div class="canvas">
  <section class="card-front">
    <span class="front-name">Kestrel Engineering</span>
  </section>

  <section class="card-back">
    <div class="brand">
      <div class="brand-square"></div>
      <span class="brand-name">Kestrel Engineering</span>
    </div>

    <div class="person">
      <div class="person-name">Daniel Marsh</div>
      <div class="person-title">SENIOR PROJECT MANAGER</div>
    </div>

    <div class="contact">
      <div><span class="label">m</span>+27 (021) 555 0142</div>
      <div><span class="label">d</span>+27 (021) 555 0187</div>
      <div><span class="label">f</span>+27 (021) 555 0193</div>
      <div>dmarsh@kestreleng.co.za</div>
    </div>

    <div class="address">
      <div>PO Box 2086,</div>
      <div>Franschhoek, 7690</div>
      <div>South Africa</div>
      <div>www.kestreleng.co.za</div>
    </div>
  </section>
</div>
</body>
</html>
```